New Architectural Firm Business Cards

New Business card to compliment previous pixel forum logo (attached). Please design a business card that is simple, modern, creative....please do not use "symbols", simply the logo and associated graphics/text. The front should contain name/address/phone/email/web address (with graphics).....back should be 100% graphic design using the logo somehow. Hoping for a two color (black and yellow) design. full bleed design, no borders

Target Market(s)

Commercial Architecture Clients

Industry/Entity Type

Architecture

Contact Information for Business Card

Please design a business card that is simple, modern, creative....please do not use "symbols", simply the logo and associated graphics/text. The front should contain name/address/phone/email/web address (with graphics).....back should be 100% graphic design using the logo somehow

Font styles to use
Sans Serif

Colors
FFF300
FFF600
FEFA6F
FFFEC7
FFFEE8

Requirements
Must have
• Clean, Modern Design
Should not have
• Stock images or "icons"

```html
<!DOCTYPE html>
<html lang="en">
<head>
<meta charset="utf-8">
<title>pixel forum — Business Card</title>
<link rel="stylesheet" href="https://fonts.googleapis.com/css2?family=Arimo:wght@400;700&display=swap">
<style>
  :root {
    --backdrop: #e6e6e4;
    --paper: #ffffff;
    --yellow: #f7c313;
    --yellow-deep: #d9a90c;
    --ink: #1a1a1a;
    --grey: #7a7a7a;
    --rule: #b5b5b5;
  }
  * { margin: 0; padding: 0; box-sizing: border-box; }
  html, body { width: 1200px; height: 802px; overflow: hidden; }
  body {
    background: var(--backdrop);
    font-family: "Arimo", Arial, sans-serif;
    display: flex;
    align-items: center;
    justify-content: center;
    gap: 48px;
  }
  .card {
    width: 525px;
    height: 300px;
    position: relative;
    overflow: hidden;
    box-shadow: 0 2px 10px rgba(0,0,0,0.12);
  }
  .card-front {
    background: var(--paper);
    display: flex;
    align-items: center;
    padding: 0 36px 0 44px;
  }
  .brand {
    width: 170px;
    display: flex;
    align-items: center;
    gap: 10px;
  }
  .brand-mark {
    width: 18px;
    height: 18px;
    background: var(--yellow);
    flex: none;
  }
  .brand-name {
    color: var(--yellow);
    font-weight: 700;
    font-size: 30px;
    line-height: 1;
    letter-spacing: -0.5px;
  }
  .divider {
    width: 1px;
    height: 150px;
    background: var(--rule);
    margin: 0 26px 0 14px;
  }
  .details { color: var(--grey); font-size: 13px; line-height: 1.35; }
  .person-name {
    color: var(--yellow);
    font-size: 19px;
    letter-spacing: 0.5px;
    text-transform: uppercase;
    margin-bottom: 2px;
  }
  .person-role { margin-bottom: 12px; }
  .address { margin-bottom: 12px; }
  .contact-list { list-style: none; }
  .contact-list li { display: flex; align-items: center; gap: 7px; }
  .contact-icon { width: 11px; height: 11px; flex: none; }
  .card-back {
    background: var(--yellow);
  }
  .back-band {
    position: absolute;
    left: 0; right: 0; bottom: 64px;
    height: 40px;
    background: #f9d04a;
  }
  .back-name {
    position: absolute;
    left: 40px;
    top: 96px;
    color: var(--yellow-deep);
    font-weight: 700;
    font-size: 76px;
    letter-spacing: -2px;
    line-height: 1;
  }
</style>
</head>
<body>

  <section class="card card-front" aria-label="Business card front">
    <div class="brand">
      <span class="brand-mark"></span>
      <span class="brand-name">pixel forum</span>
    </div>
    <div class="divider"></div>
    <div class="details">
      <p class="person-name">Daniel Hart</p>
      <p class="person-role">Manager</p>
      <p class="address">Your address, city<br>state, ZIP 0000</p>
      <ul class="contact-list">
        <li>
          <svg class="contact-icon" viewBox="0 0 12 12"><circle cx="6" cy="6" r="6" fill="#f7c313"/><path d="M3.6 3.2l1.1-.3.7 1.6-.7.5c.3.8.9 1.4 1.7 1.7l.5-.7 1.6.7-.3 1.1C6 7.9 4 6 3.6 3.2z" fill="#fff"/></svg>
          <span>123-456-2100</span>
        </li>
        <li>
          <svg class="contact-icon" viewBox="0 0 12 12"><rect x="0.5" y="2" width="11" height="8" fill="#f7c313"/><path d="M1 2.6L6 6.5l5-3.9" fill="none" stroke="#fff" stroke-width="1"/></svg>
          <span>youremail@mailbox.com</span>
        </li>
        <li>
          <svg class="contact-icon" viewBox="0 0 12 12"><circle cx="6" cy="6" r="6" fill="#f7c313"/><ellipse cx="6" cy="6" rx="2.2" ry="5" fill="none" stroke="#fff" stroke-width="0.9"/><path d="M1 6h10" stroke="#fff" stroke-width="0.9"/></svg>
          <span>www.yourwebsite.com</span>
        </li>
      </ul>
    </div>
  </section>

  <section class="card card-back" aria-label="Business card back">
    <div class="back-band"></div>
    <p class="back-name">pixel forum</p>
  </section>

</body>
</html>
```